Healthcare IT firm needs classy and unique business care design

We need a business card design that incorporates our new logo design (attached) Prefer a purple based designed. I would really love to see something utilizing the "3D" version of the logo (purple on the reflective wall). I want something a little more than my logo printed along with a person's detailed contact information.
Contact Information for Business Card
Want something polished, professional, and a little unique in the design.
Colors
6b449b
Requirements
Must have
- Please use similar font as the logo design
Nice to have
- Would like to see the 3d version of my logo incorporated into the design.

```html
<!DOCTYPE html>
<html lang="en">
<head>
<meta charset="utf-8">
<title>Veralin Health Systems – Business Card</title>
<link rel="stylesheet" href="https://fonts.googleapis.com/css2?family=Roboto:wght@400;500;700&display=swap">
<style>
  :root {
    --brand-purple: #6b449b;
    --deep-purple: #5a3589;
    --ink-purple: #3b2a5c;
    --card-white: #f4f4f4;
    --card-grey: #e2e2e2;
    --band-black: #0d0d0d;
    --stage: #dcd8d2;
    --text-white: #ffffff;
  }
  * { box-sizing: border-box; margin: 0; padding: 0; }
  html, body {
    width: 900px; height: 1200px; overflow: hidden;
    background: var(--stage);
    font-family: "Roboto", Arial, sans-serif;
  }
  .canvas { position: relative; width: 900px; height: 1200px; }

  .card {
    position: absolute; left: 88px; width: 732px; height: 427px;
    border-radius: 22px; overflow: hidden;
    box-shadow: 0 4px 10px rgba(0,0,0,0.25);
  }
  .card-front { top: 128px; background: linear-gradient(180deg, var(--card-white), var(--card-grey)); }
  .card-back { top: 641px; height: 429px; background: var(--brand-purple); }

  .front-bands { position: absolute; inset: 0; width: 732px; height: 427px; }

  .brand-mark {
    position: absolute; left: 48px; top: 42px;
    color: var(--text-white); font-weight: 700; line-height: 1;
  }
  .brand-mark .brand-name { font-size: 76px; letter-spacing: -2px; display: block; }
  .brand-mark .brand-sub { font-size: 19px; letter-spacing: 0.5px; display: block; margin-top: 8px; padding-left: 4px; }

  .holder { position: absolute; right: 45px; top: 64px; text-align: right; color: var(--text-white); }
  .holder-name { font-size: 26px; font-weight: 500; letter-spacing: 1px; }
  .holder-title { font-size: 17px; font-weight: 400; letter-spacing: 0.5px; margin-top: 4px; }

  .address {
    position: absolute; left: 44px; top: 342px;
    color: var(--ink-purple); font-size: 16.5px; line-height: 25px;
  }
  .contacts {
    position: absolute; right: 45px; top: 291px;
    list-style: none; color: var(--ink-purple); font-size: 16.5px;
  }
  .contacts li { display: flex; align-items: center; justify-content: flex-end; height: 25.5px; }
  .contacts .icon { width: 18px; height: 18px; margin-left: 10px; flex: none; }

  .back-mark {
    position: absolute; left: 0; right: 0; top: 152px;
    text-align: center; color: var(--text-white); font-weight: 700; line-height: 1;
  }
  .back-mark .brand-name { font-size: 92px; letter-spacing: -2px; display: block; }
  .back-mark .brand-sub { font-size: 22px; letter-spacing: 0.5px; display: block; margin-top: 12px; }
</style>
</head>
<body>
<main class="canvas">

  <section class="card card-front" aria-label="Business card front">
    <svg class="front-bands" viewBox="0 0 732 427" aria-hidden="true">
      <defs>
        <linearGradient id="purpleSheen" x1="0" y1="0" x2="1" y2="1">
          <stop offset="0" stop-color="#6b449b"/>
          <stop offset="1" stop-color="#5a3589"/>
        </linearGradient>
      </defs>
      <polygon points="0,0 732,0 732,200 347,204 0,255" fill="url(#purpleSheen)"/>
      <polygon points="0,255 347,204 732,200 732,209 347,212 0,264" fill="#ffffff"/>
      <polygon points="0,264 347,212 732,209 732,222 347,224 0,280" fill="var(--band-black)"/>
    </svg>

    <div class="brand-mark">
      <span class="brand-name">Veralin</span>
      <span class="brand-sub">HEALTH SYSTEMS</span>
    </div>

    <div class="holder">
      <p class="holder-name">MARCUS HALE</p>
      <p class="holder-title">MANAGING DIRECTOR</p>
    </div>

    <address class="address" style="font-style:normal">
      412 Harbor View Boulevard<br>11TH FLOOR
    </address>

    <ul class="contacts">
      <li>041-256-7390
        <svg class="icon" viewBox="0 0 18 18" aria-hidden="true"><rect width="18" height="18" rx="3" fill="var(--brand-purple)"/><path d="M5.2 4.2l2 .1.9 2.4-1.2 1a7 7 0 0 0 3.4 3.4l1-1.2 2.4.9.1 2c-.1.6-.6 1-1.2 1A9 9 0 0 1 4.2 5.4c0-.6.4-1.1 1-1.2z" fill="#fff"/></svg>
      </li>
      <li>027-118-5364
        <svg class="icon" viewBox="0 0 18 18" aria-hidden="true"><rect width="18" height="18" rx="3" fill="var(--brand-purple)"/><path d="M5.2 4.2l2 .1.9 2.4-1.2 1a7 7 0 0 0 3.4 3.4l1-1.2 2.4.9.1 2c-.1.6-.6 1-1.2 1A9 9 0 0 1 4.2 5.4c0-.6.4-1.1 1-1.2z" fill="#fff"/></svg>
      </li>
      <li>marcushale@veralin.com
        <svg class="icon" viewBox="0 0 18 18" aria-hidden="true"><rect width="18" height="18" rx="3" fill="var(--brand-purple)"/><rect x="4" y="5.5" width="10" height="7" fill="none" stroke="#fff" stroke-width="1.2"/><path d="M4 5.5l5 4 5-4" fill="none" stroke="#fff" stroke-width="1.2"/></svg>
      </li>
      <li>www.veralinhealth.com
        <svg class="icon" viewBox="0 0 18 18" aria-hidden="true"><rect width="18" height="18" rx="3" fill="var(--brand-purple)"/><g fill="none" stroke="#fff" stroke-width="1.1"><circle cx="9" cy="9" r="5"/><ellipse cx="9" cy="9" rx="2.2" ry="5"/><path d="M4 9h10M5 6.5h8M5 11.5h8"/></g></svg>
      </li>
    </ul>
  </section>

  <section class="card card-back" aria-label="Business card back">
    <div class="back-mark">
      <span class="brand-name">Veralin</span>
      <span class="brand-sub">HEALTH SYSTEMS</span>
    </div>
  </section>

</main>
</body>
</html>
```